Non-Profit org for new mothers in distress in need of website design

We need a website for our non-profit organization, Cradlewell Circle of Florida, based in Sarasota, Florida. We provide peer support for new moms in distress, trainings for mental health professionals, education and resources for our providers, and an intensive volunteer training program. We need a site that is calming yet energizing, simple, yet informative, with minimal pages and text. Our goal is to be a point of contact for mothers to find local resources whatever their need, so our most important feature we need is at least 4 zip code look-ups for users to find 1. Local volunteers, 2. Support Groups, 3. Trained Mental Health Professionals, 4. Other Health and Wellness Support Providers. Ideally I would like the zip code lookups on the home page sort of interest-layout-style, with the following pages: About Us, PPD Facts, For Parents, For Providers, Donate, Contact, and Blog. Because we are a very small non-profit - under 20 volunteers, no paid staff, donation funded, under $10,000 budget all going to service programs, we can't afford much, but are willing to pay a reasonable fee for quality work. Currently we have an active site through plexo... www.cradlewellcircle.org. The site either needs to be polished or overhauled. And we need a more professional zip code L/U. Thank you so much for your time and interest - we look forward to working with you.
Best,
Linda Varhoeven

Target Market(s)

New mothers with babies and young children, new fathers and perinatal providers

Industry/Entity Type

Non Profit

Number of Pages Required

5+ page

Font styles to use
Sans Serif

Colors
886aae

Requirements
Must have
• contact form, zip code lookup, video embedded, calm and energizing tone
Nice to have
• pinterest-style layout
Should not have
• complicated navigation, heavy text,

```html
<!DOCTYPE html>
<html lang="en">
<head>
<meta charset="utf-8">
<title>Cradlewell Circle of Florida</title>
<link rel="stylesheet" href="https://fonts.googleapis.com/css2?family=Questrial&family=Carlito:wght@400;700&family=Arimo:wght@400&display=swap">
<style>
  :root {
    --brand-blue: #0071bc;
    --accent-orange: #f7931e;
    --text-dark: #1a1a1a;
    --text-muted: #8a8a8a;
    --field-border: #6f6f6f;
    --rule-gray: #b9b9b9;
    --white: #ffffff;
    --brand-purple: #886aae;
  }
  * { box-sizing: border-box; margin: 0; padding: 0; }
  html, body { width: 1200px; height: 858px; overflow: hidden; background: var(--white); }
  body { position: relative; font-family: "Arimo", Arial, sans-serif; color: var(--text-dark); }

  .top-bar { position: absolute; left: 0; top: 0; width: 1200px; height: 16px; background: var(--brand-blue); }

  .hero { position: absolute; left: 0; top: 16px; width: 1200px; height: 452px; overflow: hidden; }
  .hero-photo {
    position: absolute; inset: 0;
    background:
      radial-gradient(ellipse 260px 220px at 680px 330px, #e9b9a0 0%, rgba(233,185,160,0) 100%),
      radial-gradient(ellipse 330px 330px at 1010px 160px, #d9a58a 0%, rgba(217,165,138,0) 100%),
      linear-gradient(90deg, #cfcfcf 0%, #e6e6e6 30%, #e2dcd8 55%, #b88f74 85%, #7a5542 100%);
  }
  .hero-message {
    position: absolute; left: 94px; top: 106px;
    font-family: "Questrial", "Century Gothic", sans-serif;
    font-size: 39px; line-height: 42px; color: var(--brand-blue);
  }
  .hero-cta {
    position: absolute; left: 98px; top: 290px; width: 335px; height: 54px;
    background: var(--brand-blue); color: var(--white);
    font-family: "Carlito", Calibri, sans-serif; font-size: 29.5px;
    display: flex; align-items: center; padding-left: 10px; white-space: nowrap;
  }
  .slider-arrow {
    position: absolute; top: 207px; width: 37px; height: 47px;
    display: flex; align-items: center; justify-content: center;
    color: var(--white); font-family: "Arimo", sans-serif; font-size: 30px;
  }
  .slider-arrow.prev { left: 10px; background: rgba(120,120,120,0.55); }
  .slider-arrow.next { left: 1155px; background: rgba(60,40,30,0.25); }
  .slider-dots { position: absolute; left: 989px; top: 423px; display: flex; gap: 7px; }
  .slider-dots span { width: 16px; height: 16px; border-radius: 50%; background: rgba(255,255,255,0.85); }
  .slider-dots span.current { background: rgba(255,255,255,0.35); }

  .main-nav {
    position: absolute; left: 127px; top: 468px; width: 1073px; height: 42px;
    background: var(--brand-blue);
  }
  .main-nav a {
    position: absolute; top: 0; height: 42px; line-height: 42px;
    transform: translateX(-50%); white-space: nowrap;
    color: var(--white); text-decoration: none;
    font-family: "Carlito", Calibri, sans-serif; font-size: 18px;
  }
  .nav-search { position: absolute; left: 990px; top: 11px; }

  .brand-badge {
    position: absolute; left: 9px; top: 428px; width: 119px; height: 124px;
    background: var(--white);
    border-right: 3px solid var(--brand-blue); border-bottom: 3px solid var(--brand-blue);
    display: flex; flex-direction: column; align-items: center; justify-content: center; gap: 8px;
    font-family: "Carlito", Calibri, sans-serif; font-size: 17px; color: var(--brand-purple);
    text-align: center; line-height: 18px;
  }
  .brand-badge .badge-dot { width: 26px; height: 26px; border-radius: 50%; background: var(--brand-purple); }

  .volunteer-finder { position: absolute; left: 0; top: 560px; width: 598px; }
  .volunteer-title {
    position: absolute; left: 29px; top: 9px; white-space: nowrap;
    font-family: "Carlito", Calibri, sans-serif; font-weight: 700; font-size: 26px;
    color: var(--brand-blue);
  }
  .volunteer-intro {
    position: absolute; left: 34px; top: 47px; width: 560px;
    font-size: 17.6px; line-height: 21.7px; color: var(--text-dark); white-space: nowrap;
  }
  .zip-search {
    display: flex; overflow: hidden;
    border: 1.5px solid var(--field-border);
  }
  .zip-search .zip-field { display: flex; align-items: center; color: var(--text-muted); }
  .zip-search .zip-submit {
    flex: 1; background: var(--accent-orange); color: var(--white);
    display: flex; align-items: center; justify-content: center;
  }
  .volunteer-finder .zip-search {
    position: absolute; left: 48px; top: 184px; width: 483px; height: 57px; border-radius: 29px;
  }
  .volunteer-finder .zip-field { width: 310px; padding-left: 61px; font-size: 24px; }
  .volunteer-finder .zip-submit { font-size: 25px; }

  .section-divider { position: absolute; left: 597px; top: 540px; width: 2px; height: 267px; background: var(--rule-gray); }

  .resource-finders { position: absolute; left: 640px; top: 545px; width: 520px; }
  .resource-lookup { position: absolute; left: 0; width: 520px; height: 80px; }
  .resource-title {
    font-size: 20px; font-weight: 400; color: var(--brand-blue); white-space: nowrap; line-height: 24px;
  }
  .resource-lookup .zip-search {
    position: absolute; left: 0; top: 31px; width: 480px; height: 44px; border-radius: 22px;
  }
  .resource-lookup .zip-field { width: 300px; padding-left: 36px; font-size: 18px; }
  .resource-lookup .zip-submit { font-size: 19px; }

  .footer-rule { position: absolute; left: 0; top: 815px; width: 1200px; height: 2px; background: #d0d0d0; }
</style>
</head>
<body>
  <div class="top-bar"></div>

  <section class="hero">
    <div class="hero-photo" role="img" aria-label="Photo of a mother gently touching her nose to her sleeping newborn's cheek"></div>
    <p class="hero-message">You are not alone.<br>You are not to blame.<br>With help and effort,<br>you will be well.</p>
    <div class="hero-cta">We can Help, Contact Us!</div>
    <div class="slider-arrow prev">&lt;</div>
    <div class="slider-arrow next">&gt;</div>
    <div class="slider-dots"><span class="current"></span><span></span><span></span><span></span><span></span></div>
  </section>

  <nav class="main-nav">
    <a style="left:66px">Home</a>
    <a style="left:184px">About Us,</a>
    <a style="left:300px">PPD Facts</a>
    <a style="left:420px">For Parents</a>
    <a style="left:548px">For Providers</a>
    <a style="left:670px">Donate</a>
    <a style="left:780px">Contact</a>
    <a style="left:888px">Blog</a>
    <svg class="nav-search" width="26" height="18" viewBox="0 0 26 18" aria-label="Search">
      <circle cx="7" cy="7" r="6" fill="none" stroke="#fff" stroke-width="1.6"/>
      <line x1="12" y1="10" x2="24" y2="16" stroke="#fff" stroke-width="1.6"/>
    </svg>
  </nav>

  <div class="brand-badge">
    <span class="badge-dot"></span>
    <span>Cradlewell<br>Circle</span>
  </div>

  <section class="volunteer-finder">
    <h2 class="volunteer-title">Find your Cradlewell Circle Mom Volunteer</h2>
    <p class="volunteer-intro">today with the locator below.&nbsp; Your area CircleMom will listen,<br>connect you with Support Groups, counselors, therapists &amp;<br>psychiatrists with training in PPD near you, doulas, wellness<br>and more to encourage your PPD recovery. Your CircleMom<br>is a trained volunteer and PPD overcomer - call or email her today.</p>
    <div class="zip-search">
      <div class="zip-field">Enter ZIP Code</div>
      <div class="zip-submit">SEARCH</div>
    </div>
  </section>

  <div class="section-divider"></div>

  <section class="resource-finders">
    <div class="resource-lookup" style="top:0">
      <h2 class="resource-title">Find a Mom-to-Mom Support Group</h2>
      <div class="zip-search"><div class="zip-field">Enter ZIP Code</div><div class="zip-submit">SEARCH</div></div>
    </div>
    <div class="resource-lookup" style="top:88px">
      <h2 class="resource-title">Find a Trained Mental Health Professional</h2>
      <div class="zip-search"><div class="zip-field">Enter ZIP Code</div><div class="zip-submit">SEARCH</div></div>
    </div>
    <div class="resource-lookup" style="top:176px">
      <h2 class="resource-title">Find Health &amp; Wellness Support Providers</h2>
      <div class="zip-search"><div class="zip-field">Enter ZIP Code</div><div class="zip-submit">SEARCH</div></div>
    </div>
  </section>

  <div class="footer-rule"></div>
</body>
</html>
```